Interior Design & Furniture E commerce Website Design

I need a cutting edge website design, this is for Interior Design Services as well as eCommerce for furniture and home decor www.lorivelhomestudio.com
Here is a sample of the concept behind the site.
I am a furniture & Interior Designer, want to create a life style brand.
Will offer Interior Design Services : Commercial & Residential (this portion will be a catalog or portfolio type)
The eCommerce side will sell, Furniture, Lighting, Decor, Gifts, Textiles, will also be offering trade so that could be at bottom of site. I also like the concept of concierge as where all the info falls under: shipping, etc..

*Please make sure to make the eCommerce prominent.

Hello Designers, I also would like to possibly update my logo, the current one I like but don't Love.

Target Market(s)

High end customers with disposable income, who also appreciate quality and unique furniture & design

Number of Pages Required

5+ page

Colors
0255a3
f37122

Requirements
Must have
• Room Planer: I will be using this tool http://qtstudio.varnelbex.com/room-planner.inc
• Live Chat
• Will be offering 3d renderings for spaces as well as Virtual Reality
• The image I loaded that looks like copper, I would like to have that as a color on the site with the texture: so the colors are Blue and copper. Would like the site to be user friendly and interactive
• http://qtstudio.varnelbex.com/ (this is the current site in development, so we will be offering Design your own, Trends, inspiration, etc...
• I have included a headshot to use for now about me. or about us.
• I also included several actual project installation (residential and commercial) as well as a variety of my furniture items
• I have Included an old Bio and some articles I would like to show case in a Press Area
• I would also like to include a section for Events (Giving back )I do a lot of charity events 1-2 a year and would like to showcase that as well
• *Please make the store (ecommerce prominent )

```html
<!DOCTYPE html>
<html lang="en">
<head>
<meta charset="utf-8">
<title>Lorivel Home Studio — Furniture &amp; Interior Design</title>
<link href="https://fonts.googleapis.com/css2?family=Poppins:wght@300;400;500;600;700&display=swap" rel="stylesheet">
<style>
:root{
  --blue:#4a72d4;
  --blue-soft:#9fb1e6;
  --orange:#f5a623;
  --yellow:#ffe500;
  --ink:#2b2b2b;
  --muted:#8a8a8a;
  --light:#f4f4f6;
  --hero:#eeeff2;
  --dark:#1b1b1b;
  --footer:#161616;
  --white:#ffffff;
}
*{box-sizing:border-box;margin:0;padding:0}
html,body{width:1200px;height:3391px;overflow:hidden}
body{font-family:'Poppins',sans-serif;color:var(--ink);background:var(--white);position:relative}
.abs{position:absolute}
a{color:inherit;text-decoration:none}

/* top bar */
.topbar{left:0;top:0;width:1200px;height:40px;background:var(--blue);color:var(--white);font-size:11px}
.topbar .promo{left:72px;top:13px}
.topbar .promo b{color:var(--yellow);font-weight:600}
.topbar .tools{right:72px;top:7px;display:flex;align-items:center;gap:18px}
.login-btn{background:var(--yellow);color:var(--ink);font-size:10px;font-weight:600;padding:6px 14px;border-radius:3px}

/* hero */
.hero{left:0;top:40px;width:1200px;height:600px;background:var(--hero);overflow:hidden}
.logo{left:136px;top:16px;width:120px;height:90px;display:flex;flex-direction:column;align-items:center;justify-content:center;gap:6px}
.logo .mark{width:30px;height:30px;border:2px solid #b49a6a}
.logo .name{font-size:15px;font-weight:600;color:#b49a6a;letter-spacing:1px}
.nav{left:528px;top:43px;display:flex;gap:26px;font-size:12px;font-weight:500}
.nav .active{border-bottom:2px solid var(--blue);padding-bottom:4px}
.hero-title{left:136px;top:160px}
.hero-title .lead{font-size:40px;font-weight:400;line-height:48px}
.hero-title .big{font-size:44px;font-weight:600;color:var(--orange);line-height:54px}
.hero-title .brace{left:264px;top:42px;font-size:110px;font-weight:300;line-height:110px}
.hero-title .role{left:308px;top:86px;font-size:34px;font-weight:600;white-space:nowrap}
.hero-bio{left:136px;top:332px;width:440px;font-size:11px;line-height:20px;color:#555}
.socials{display:flex;gap:10px}
.socials span{width:16px;height:16px;border-radius:2px;display:block}
.hero .socials{left:136px;top:440px}
.btn-blue{background:var(--blue);color:var(--white);font-size:11px;font-weight:600;border-radius:20px;padding:10px 48px}
.hero .btn-blue{left:136px;top:478px}
.portrait{left:680px;top:0;width:380px;height:380px;border-radius:50%;background:radial-gradient(circle at 50% 40%,#8a8a8a,#3a3a3a 75%)}
.slider-arrow{width:30px;height:30px;border-radius:50%;background:#d9dbe2;display:flex;align-items:center;justify-content:center}

/* section heading */
.sec-head{left:0;width:1200px;text-align:center}
.sec-head h2{font-size:14px;font-weight:600}
.sec-head .sub{font-size:10px;color:var(--muted);margin-top:4px}
.sec-head p{font-size:11px;color:var(--muted);line-height:22px;width:620px;margin:8px auto 0}

/* services grid */
.tile{overflow:hidden}
.tile-label{background:var(--white);font-size:10px;font-weight:500;padding:12px 22px;position:absolute;white-space:nowrap}

/* design band */
.design-band{left:0;top:1202px;width:1200px;height:229px}
.band-text{color:var(--white);text-align:center;font-weight:700;font-size:22px;line-height:28px}
.band-text .hl{color:var(--yellow)}

/* products */
.products-head{left:136px;top:1462px}
.products-head h2{font-size:13px;font-weight:600}
.products-head p{font-size:10px;color:var(--muted);margin-top:6px}
.view-all{left:998px;top:1479px;background:var(--blue);color:var(--white);font-size:9px;font-weight:600;padding:5px 16px;border-radius:12px}
.product{width:203px;text-align:center}
.product .photo{width:203px;height:202px;background:var(--light);position:relative}
.product .photo .art{position:absolute;left:40px;top:40px;width:123px;height:122px;border-radius:8px}
.product .title{font-size:11px;font-weight:500;margin-top:12px}
.product .price{font-size:10px;font-weight:600;margin-top:6px}
.quick{position:absolute;bottom:16px;left:0;width:100%;display:flex;justify-content:center;gap:14px}
.quick span{width:30px;height:30px;border-radius:50%;background:var(--white);box-shadow:0 1px 4px rgba(0,0,0,.15);display:flex;align-items:center;justify-content:center}

/* vr band */
.vr{left:0;top:2100px;width:1200px;height:470px}
.vr-copy{left:0;top:2252px;width:1200px;text-align:center;color:var(--white)}
.vr-copy .line{font-size:30px;font-weight:700;line-height:44px}
.vr-copy .line .hl{color:var(--yellow)}
.vr-copy .tag{display:inline-block;font-size:15px;font-weight:600;margin-top:16px;padding-bottom:6px;border-bottom:2px solid var(--white)}

/* projects */
.project{left:134px;top:2694px;width:932px;height:358px;background:linear-gradient(120deg,#6d5a4a,#a89a8a 40%,#c7b9a9 60%,#5b4a46);overflow:hidden}
.project-copy{left:100px;top:102px;width:340px;color:var(--white)}
.project-copy h3{font-size:15px;font-weight:600}
.project-copy p{font-size:10px;line-height:18px;margin-top:14px}
.project-copy .more{font-size:10px;margin-top:18px;display:flex;align-items:center;gap:10px}
.project-copy .more i{display:block;width:50px;height:1px;background:var(--white)}

/* footer */
.footer{left:0;top:3094px;width:1200px;height:297px;background:var(--footer);color:var(--white)}
.footer h4{font-size:13px;font-weight:600}
.footer .info{font-size:10px;color:#8c8c8c;line-height:17px;margin-top:14px}
.directions{left:920px;top:45px;width:141px;height:40px;border:1px solid #555;border-radius:4px;display:flex;align-items:center;justify-content:center;gap:8px;font-size:10px}
.phone{left:884px;top:106px;display:flex;align-items:center;gap:10px;font-size:20px;font-weight:600}
.foot-rule{left:136px;top:167px;width:928px;height:1px;background:#2e2e2e}
.foot-links{left:136px;top:186px;display:flex;gap:20px;font-size:9px;color:#777}
.copyright{right:136px;top:186px;font-size:9px;color:#777}
</style>
</head>
<body>

<header class="abs topbar">
  <div class="abs promo">Pop up your own LUMA Pavilion for <b>ONLY $99</b></div>
  <div class="abs tools">
    <svg width="14" height="14" viewBox="0 0 14 14"><circle cx="6" cy="6" r="4.5" fill="none" stroke="#ffe500" stroke-width="2"/><line x1="9.5" y1="9.5" x2="13" y2="13" stroke="#ffe500" stroke-width="2"/></svg>
    <svg width="15" height="14" viewBox="0 0 15 14"><path d="M7.5 13 1.5 7A3.5 3.5 0 0 1 7.5 2.5 3.5 3.5 0 0 1 13.5 7Z" fill="#ffe500"/></svg>
    <svg width="16" height="15" viewBox="0 0 16 15"><path d="M1 1h3l2 9h8l1.5-6H5" fill="none" stroke="#fff" stroke-width="1.6"/><circle cx="7" cy="13" r="1.3" fill="#fff"/><circle cx="13" cy="13" r="1.3" fill="#fff"/></svg>
    <span class="login-btn">🔒 LOGIN / SIGNUP</span>
  </div>
</header>

<section class="abs hero">
  <svg class="abs" style="left:0;top:0" width="1200" height="600" viewBox="0 0 1200 600">
    <polygon points="0,0 420,0 260,260 0,180" fill="#f3f4f6"/>
    <polygon points="420,0 900,0 640,230" fill="#e8e9ed"/>
    <polygon points="0,180 260,260 120,520 0,470" fill="#e6e7eb"/>
    <polygon points="900,0 1200,0 1200,300 1020,210" fill="#f1f2f5"/>
    <polygon points="640,230 1020,210 1200,300 1200,520 760,560" fill="#e9eaee"/>
    <polygon points="0,600 0,470 330,560 600,500 1200,520 1200,600" fill="#ffffff"/>
    <polygon points="330,560 600,500 640,600 380,600" fill="#f7f7f9"/>
  </svg>
  <div class="abs logo"><span class="mark"></span><span class="name">LORIVEL</span></div>
  <nav class="abs nav">
    <a class="active">Home</a><a>Furniture</a><a>Lighting</a><a>Decor</a><a>Gifts</a><a>Textiles</a><a>About me</a><a>Contact me</a>
  </nav>
  <div class="abs hero-title">
    <div class="lead">I am a</div>
    <div class="big">FURNITURE</div>
    <div class="big">INTERIOR</div>
    <div class="abs brace">}</div>
    <div class="abs role">DESIGNER</div>
  </div>
  <p class="abs hero-bio">Elena Varga Morrow is Vice President and Furniture Designer of Harborline Hospitality Design, Inc. She has over 20 years of experience in the furniture manufacturing industry ranging from design concept, manufacturing, production to research and development.</p>
  <div class="abs socials">
    <span style="background:#3fa9e0"></span><span style="background:#f39a2b"></span><span style="background:#3b5b98"></span><span style="background:#555"></span><span style="background:#333"></span><span style="background:#d6323a"></span>
  </div>
  <a class="abs btn-blue">know more about me</a>
  <div class="abs portrait" style="top:110px" role="img" aria-label="Portrait photo of the designer"></div>
  <svg class="abs" style="left:600px;top:340px" width="140" height="180" viewBox="0 0 140 180">
    <circle cx="34" cy="20" r="8" fill="#b7c3ec"/>
    <circle cx="68" cy="122" r="26" fill="#b7c3ec"/>
    <circle cx="50" cy="150" r="8" fill="#b7c3ec"/>
    <circle cx="96" cy="166" r="10" fill="#b7c3ec"/>
  </svg>
  <div class="abs slider-arrow" style="left:80px;top:286px"><svg width="10" height="10"><path d="M7 1 3 5l4 4" fill="none" stroke="#fff" stroke-width="2"/></svg></div>
  <div class="abs slider-arrow" style="left:1096px;top:286px"><svg width="10" height="10"><path d="M3 1l4 4-4 4" fill="none" stroke="#fff" stroke-width="2"/></svg></div>
</section>

<section class="abs sec-head" style="top:660px">
  <h2>WHAT WE CAN OFFER YOU</h2>
  <div class="sub">MADE THE HARD WAY</div>
  <p>Lorem ipsum dolor sit amet, consectetuer adipiscing elit. Aenean commodo ligula eget dolor. Aenean massa. Cum sociis natoque penatibus et magnis</p>
</section>

<div class="abs tile" style="left:134px;top:779px;width:431px;height:372px;background:#f0f0f2">
  <div class="abs" style="left:70px;top:60px;width:300px;height:220px;border-radius:20px;background:linear-gradient(135deg,#5d7fd0,#2e4f9f 60%,#4a2f22)" role="img" aria-label="Blue upholstered chaise lounge on wooden legs"></div>
  <span class="tile-label" style="left:130px;top:308px">FURNITURE</span>
</div>
<div class="abs tile" style="left:584px;top:779px;width:228px;height:174px;background:linear-gradient(160deg,#6a3a2c,#c08a6a 50%,#4a2a22)" role="img" aria-label="Living room interior with fireplace">
  <span class="tile-label" style="left:46px;top:124px">INTERIOR DESIGN</span>
</div>
<div class="abs tile" style="left:584px;top:976px;width:228px;height:175px;background:linear-gradient(135deg,#5a5048,#9a8a7a 50%,#3e3630)" role="img" aria-label="Top-down view of a furnished room plan">
  <span class="tile-label" style="left:52px;top:124px">ROOM PLAANER</span>
</div>
<div class="abs tile" style="left:838px;top:779px;width:228px;height:372px;background:linear-gradient(180deg,#4a3c30,#8a7a66 50%,#bfb4a4)" role="img" aria-label="Hanging glass pendant lights">
  <span class="tile-label" style="left:52px;top:326px">ROOM PLAANER</span>
</div>

<section class="abs design-band">
  <svg class="abs" style="left:0;top:0" width="1200" height="229" viewBox="0 0 1200 229">
    <defs>
      <linearGradient id="commercialTone" x1="0" y1="0" x2="1" y2="1"><stop offset="0" stop-color="#3c4a62"/><stop offset="1" stop-color="#1e2636"/></linearGradient>
      <linearGradient id="residentialTone" x1="0" y1="0" x2="1" y2="1"><stop offset="0" stop-color="#5a2622"/><stop offset="1" stop-color="#231210"/></linearGradient>
    </defs>
    <polygon points="0,0 560,0 505,114 560,229 0,229" fill="url(#commercialTone)" role="img" aria-label="Commercial office interior photo"/>
    <polygon points="560,0 1200,0 1200,229 560,229 505,114" fill="url(#residentialTone)" role="img" aria-label="Residential lounge interior photo"/>
  </svg>
  <div class="abs band-text" style="left:170px;top:80px;width:360px"><span class="hl">COMMERCIAL</span><br>INTERIOR DESIGN</div>
  <div class="abs band-text" style="left:660px;top:80px;width:360px"><span class="hl">RESIDENTAL</span><br>INTERIOR DESIGN</div>
  <svg class="abs" style="left:337px;top:160px" width="26" height="14"><path d="M0 7h24M18 1l6 6-6 6" fill="none" stroke="#fff" stroke-width="2"/></svg>
  <svg class="abs" style="left:827px;top:160px" width="26" height="14"><path d="M0 7h24M18 1l6 6-6 6" fill="none" stroke="#fff" stroke-width="2"/></svg>
</section>

<div class="abs products-head">
  <h2>OUR LATEST PRODUCTS</h2>
  <p>The most prominent product in the store, which was bought with the highest number</p>
</div>
<a class="abs view-all">View All</a>

<div class="abs product" style="left:134px;top:1546px"><div class="photo"><div class="art" style="background:linear-gradient(135deg,#a8926a,#5a4830)" role="img" aria-label="Carved bronze side table"></div></div><div class="title">Starsmall</div><div class="price">$ 115.00</div></div>
<div class="abs product" style="left:369px;top:1546px"><div class="photo"><div class="art" style="background:linear-gradient(135deg,#7c9be0,#3c5cb0)" role="img" aria-label="Blue chaise chair"></div>
  <div class="quick"><span><svg width="12" height="11"><path d="M6 10 1.2 5.5A2.6 2.6 0 0 1 6 2a2.6 2.6 0 0 1 4.8 3.5Z" fill="none" stroke="#555"/></svg></span><span><svg width="12" height="12"><circle cx="5" cy="5" r="3.5" fill="none" stroke="#555"/><line x1="8" y1="8" x2="11" y2="11" stroke="#555"/></svg></span><span><svg width="12" height="12"><path d="M0.5 1h2l1.5 7h6l1-5H3.5" fill="none" stroke="#555"/></svg></span></div></div>
  <div class="title">DSC Chair</div><div class="price">$ 115.00</div></div>
<div class="abs product" style="left:616px;top:1546px"><div class="photo"><div class="art" style="background:linear-gradient(135deg,#5a5a5a,#2a2a2a)" role="img" aria-label="Woven outdoor sofa"></div></div><div class="title">Coral sofa</div><div class="price">$ 255.00</div></div>
<div class="abs product" style="left:864px;top:1546px"><div class="photo"><div class="art" style="background:linear-gradient(135deg,#c9c1b4,#8a7e6e)" role="img" aria-label="Upholstered lounge armchair"></div></div><div class="title">Starsmall</div><div class="price">$ 58.00</div></div>

<div class="abs product" style="left:134px;top:1831px"><div class="photo"><div class="art" style="background:linear-gradient(135deg,#d6d2c2,#9c957e)" role="img" aria-label="Textured throw pillow"></div></div><div class="title">Starsmall</div><div class="price">$ 115.00</div></div>
<div class="abs product" style="left:369px;top:1831px"><div class="photo"><div class="art" style="background:linear-gradient(135deg,#4a2418,#c23a2a)" role="img" aria-label="Dark wood chair with red cushion"></div></div><div class="title">DSC Chair</div><div class="price">$ 115.00</div></div>
<div class="abs product" style="left:616px;top:1831px"><div class="photo"><div class="art" style="background:linear-gradient(135deg,#a7a29a,#7a6448)" role="img" aria-label="Pair of upholstered stools"></div></div><div class="title">Coral sofa</div><div class="price">$ 255.00</div></div>
<div class="abs product" style="left:864px;top:1831px"><div class="photo"><div class="art" style="background:linear-gradient(135deg,#8a8a8a,#e0a43a)" role="img" aria-label="Grey daybed with orange stripe"></div></div><div class="title">Starsmall</div><div class="price">$ 58.00</div></div>

<section class="abs vr">
  <svg class="abs" style="left:0;top:0" width="1200" height="470" viewBox="0 0 1200 470" role="img" aria-label="Dim studio photo of designer reviewing floor plans">
    <defs><linearGradient id="studioTone" x1="0" y1="0" x2="1" y2="0"><stop offset="0" stop-color="#2a2a2a"/><stop offset=".5" stop-color="#3d3d3d"/><stop offset="1" stop-color="#1a1a1a"/></linearGradient></defs>
    <polygon points="0,50 420,0 1200,60 1200,430 720,470 0,400" fill="url(#studioTone)"/>
  </svg>
  <div class="abs vr-copy" style="top:152px">
    <div class="line">WE offering <span class="hl">3D RENDERINGS</span> for spaces</div>
    <div class="line">as well as <span class="hl">VIRTUAL REALITY</span></div>
    <div class="tag">NEW IN OUR TECHNOLOGIES</div>
  </div>
  <svg class="abs" style="left:542px;top:314px" width="70" height="70" viewBox="0 0 70 70"><circle cx="35" cy="35" r="32" fill="none" stroke="#fff" stroke-width="4"/><path d="M28 22v26l20-13Z" fill="#fff"/></svg>
</section>

<section class="abs sec-head" style="top:2592px">
  <h2>OUR PROJECTS WORKS SO FAR</h2>
  <div class="sub">Gallery &amp; Portfolio</div>
  <p>Lorem ipsum dolor sit amet, consectetuer adipiscing elit. Aenean commodo ligula eget dolor. Aenean massa. Cum sociis natoque penatibus et magnis , Lorem ipsum dolor sit amet, consectetuer adipiscing elit.</p>
</section>

<div class="abs project" role="img" aria-label="Bright kitchen bar with red stools and checkered floor">
  <div class="abs" style="left:0;top:0;width:560px;height:358px;background:linear-gradient(90deg,rgba(0,0,0,.55),rgba(0,0,0,0))"></div>
  <div class="abs project-copy">
    <h3>The Elegant Home</h3>
    <p>Lorem ipsum dolor sit amet, consectetuer adipiscing elit. Aenean commodo ligula eget dolor. Aenean massa. Cum sociis natoque penatibus et magnis , Lorem ipsum dolor sit amet, consectetuer adipiscing elit. Aenean commodo ligula eget dolor. Aenean massa.</p>
    <div class="more">more info <i></i></div>
  </div>
  <svg class="abs" style="left:56px;top:170px" width="20" height="20"><circle cx="10" cy="10" r="9" fill="none" stroke="#fff"/><path d="M11.5 6 7.5 10l4 4" fill="none" stroke="#fff" stroke-width="1.5"/></svg>
  <svg class="abs" style="left:862px;top:170px" width="20" height="20"><circle cx="10" cy="10" r="9" fill="none" stroke="#fff"/><path d="M8.5 6l4 4-4 4" fill="none" stroke="#fff" stroke-width="1.5"/></svg>
</div>

<footer class="abs footer">
  <div class="abs" style="left:136px;top:56px">
    <h4>VISIT OUR SHOWROOM</h4>
    <div class="info">418 Corvel Ave, Brookhaven, NY 10482, USA<br>Mon - Sat : 10 am - 6 pm &nbsp;&nbsp;|&nbsp;&nbsp; Sun : 12 pm - 2 pm</div>
  </div>
  <div class="abs socials" style="left:544px;top:76px;gap:16px">
    <span style="background:#3b5b98"></span><span style="background:#3fa9e0"></span><span style="background:#f39a2b"></span><span style="background:#d6323a"></span><span style="background:#4a86c5"></span>
  </div>
  <div class="abs directions"><svg width="10" height="13" viewBox="0 0 10 13"><path d="M5 12.5S.5 7.5.5 4.8a4.5 4.5 0 0 1 9 0C9.5 7.5 5 12.5 5 12.5Z" fill="#fff"/><circle cx="5" cy="4.8" r="1.6" fill="#161616"/></svg>Get Directions</div>
  <div class="abs phone"><svg width="22" height="22" viewBox="0 0 24 24"><path d="M6.6 10.8a15 15 0 0 0 6.6 6.6l2.2-2.2a1 1 0 0 1 1-.25 11.4 11.4 0 0 0 3.6.57 1 1 0 0 1 1 1V20a1 1 0 0 1-1 1A17 17 0 0 1 3 4a1 1 0 0 1 1-1h3.5a1 1 0 0 1 1 1 11.4 11.4 0 0 0 .57 3.6 1 1 0 0 1-.25 1Z" fill="none" stroke="#fff" stroke-width="1.6"/></svg>333.410.05718</div>
  <div class="abs foot-rule"></div>
  <nav class="abs foot-links"><a>Home</a><a>Furniture</a><a>Lighting</a><a>Decor</a><a>Gifts</a><a>Textiles</a><a>About me</a><a>Contact me</a></nav>
  <div class="abs copyright">Copyright © 2018 LORIVEL HOME STUDIO LLC All Rights Reserved</div>
</footer>

</body>
</html>
```